Kinesiology undergraduate program needs an infographic

We would like an infographic to creatively and succinctly inform students, faculty, staff, and others about our undergraduate values and competencies (perhaps also integrating our mission and vision). We would like to see a design that incorporates the definition of Kinesiology (the study of human movement) and the colors of our Northbrook Lakeshore State University.

```html
<!DOCTYPE html>
<html lang="en">
<head>
<meta charset="utf-8">
<title>The Science of Kinesiology — NLSU Undergraduate Program</title>
<link href="https://fonts.googleapis.com/css2?family=Poppins:wght@400;500;800&display=swap" rel="stylesheet">
<style>
  :root{
    --teal-blue:#0180a7;
    --navy:#001a5e;
    --crimson:#d40036;
    --olive:#8b9a00;
    --white:#ffffff;
    --orange:#e99a22;
    --green:#17876e;
    --ink-blue:#0c7fa6;
  }
  *{margin:0;padding:0;box-sizing:border-box}
  html,body{width:678px;height:1200px;overflow:hidden}
  body{font-family:"Poppins",sans-serif;color:var(--white);position:relative;background:var(--white)}
  .band{position:absolute}
  .science{left:0;top:0;width:339px;height:659px;background:var(--teal-blue)}
  .mission{left:339px;top:0;width:339px;height:127px;background:var(--navy)}
  .vision{left:339px;top:127px;width:339px;height:127px;background:var(--crimson)}
  .values{left:339px;top:254px;width:339px;height:127px;background:var(--olive)}
  .thinking{left:339px;top:381px;width:339px;height:278px;background:var(--white)}
  .relationships{left:0;top:659px;width:678px;height:270px;background:var(--orange)}
  .growth{left:0;top:929px;width:678px;height:271px;background:var(--green)}

  .art{position:absolute;border-radius:50%}
  .heading{font-weight:800;line-height:1.0;letter-spacing:-0.3px}
  .center{position:absolute;left:0;right:0;text-align:center}

  /* science column */
  .anatomy-display{position:absolute;left:51px;top:48px;width:237px;height:249px;border-radius:6px;
    background:linear-gradient(180deg,#f2f2f2 0%,#e4e4e4 55%,rgba(228,228,228,.35) 60%,rgba(255,255,255,.08) 100%)}
  .science .heading{top:318px;font-size:26px}
  .topic{position:absolute;left:151px;font-size:14px;line-height:17px}
  .topic-art{position:absolute;left:68px;width:56px;height:56px}

  /* statements */
  .statement{position:absolute;left:128px;top:18px;right:10px}
  .statement h2{font-weight:800;font-size:18px;line-height:22px}
  .statement p,.statement li{font-size:10.5px;line-height:12.4px}
  .statement ul{list-style:none;margin-top:4px}
  .statement li{display:flex;align-items:center;gap:3px}
  .statement li svg{width:9px;height:9px;flex:none}
  .statement-art{position:absolute;left:36px;top:32px;width:62px;height:62px}

  /* thinking */
  .thinking .heading{top:32px;font-size:26px;color:var(--ink-blue)}
  .skill{position:absolute;font-size:14px;line-height:17px;color:var(--ink-blue)}
  .skill-art{position:absolute;width:58px;height:58px}

  /* rows */
  .row-heading{font-size:26px}
  .row-item{position:absolute;width:150px;text-align:center;font-size:14px;line-height:17px}
  .row-art{position:absolute;width:60px;height:60px}
</style>
</head>
<body>

<section class="band science">
  <div class="anatomy-display" role="img" aria-label="Projection screen on a tripod showing front, back and side views of human muscle anatomy"></div>
  <h1 class="heading center">The Science of<br>Kinesiology</h1>

  <div class="topic-art art" style="top:382px;height:88px;border-radius:30%;background:#c8102e" role="img" aria-label="Red human figure with highlighted joints"></div>
  <p class="topic" style="top:400px">Foundational<br>Concepts of<br>Kinesiology</p>

  <div class="topic-art" style="top:494px;border-radius:10px;background:linear-gradient(#f6c56f,#f0a23b)" role="img" aria-label="Bandage roll with medical cross"></div>
  <p class="topic" style="top:500px">Clinical<br>Application</p>

  <div class="topic-art art" style="top:568px;background:radial-gradient(circle,#d9d9d9 45%,#f0a23b 46%,#f0a23b 52%,transparent 53%)" role="img" aria-label="Atom with orbiting electrons"></div>
  <p class="topic" style="top:585px">Scientific<br>Communication</p>
</section>

<section class="band mission">
  <div class="statement-art art" style="background:linear-gradient(135deg,#ffffff 40%,#e0234e 60%,#f6a21a)" role="img" aria-label="Rocket launching"></div>
  <div class="statement">
    <h2>Our Mission</h2>
    <p>To empower undergraduate students<br>to pursue excellence through</p>
    <ul>
      <li><svg viewBox="0 0 10 10"><path d="M1 5.5 4 8.5 9 1.5" fill="none" stroke="#fff" stroke-width="2"/></svg>Scientific Discovery</li>
      <li><svg viewBox="0 0 10 10"><path d="M1 5.5 4 8.5 9 1.5" fill="none" stroke="#fff" stroke-width="2"/></svg>Clinical Practice</li>
      <li><svg viewBox="0 0 10 10"><path d="M1 5.5 4 8.5 9 1.5" fill="none" stroke="#fff" stroke-width="2"/></svg>Health Promotion</li>
    </ul>
  </div>
</section>

<section class="band vision">
  <div class="statement-art art" style="background:radial-gradient(circle,#f6a623 50%,transparent 52%)" role="img" aria-label="Glowing light bulb"></div>
  <div class="statement" style="top:27px">
    <h2>Our Vision</h2>
    <p>NLSU Kinesiology graduates are<br>leaders who excel in careers that<br>enhance the quality of life of<br>individuals and communities.</p>
  </div>
</section>

<section class="band values">
  <div class="statement-art" style="top:30px;border-radius:12px;background:linear-gradient(#f7c9a0,#e8a070)" role="img" aria-label="Two hands cradling a heart"></div>
  <div class="statement" style="top:27px">
    <h2>Our Values</h2>
    <ul>
      <li><svg viewBox="0 0 10 10"><path d="M1 5.5 4 8.5 9 1.5" fill="none" stroke="#fff" stroke-width="2"/></svg>Student Success</li>
      <li><svg viewBox="0 0 10 10"><path d="M1 5.5 4 8.5 9 1.5" fill="none" stroke="#fff" stroke-width="2"/></svg>Science</li>
      <li><svg viewBox="0 0 10 10"><path d="M1 5.5 4 8.5 9 1.5" fill="none" stroke="#fff" stroke-width="2"/></svg>Service</li>
    </ul>
  </div>
</section>

<section class="band thinking">
  <h2 class="heading center">Thinking and<br>Reasoning</h2>
  <div class="skill-art art" style="left:22px;top:108px;background:#e2565e" role="img" aria-label="Head filled with ideas and science tools"></div>
  <p class="skill" style="left:89px;top:118px">Critical<br>Thinking</p>
  <div class="skill-art" style="left:183px;top:108px;border-radius:12px;background:linear-gradient(135deg,#e0565e,#1f5fa8)" role="img" aria-label="Microscope with sample dish"></div>
  <p class="skill" style="left:244px;top:118px">Scientific<br>Inquiry</p>
  <div class="skill-art" style="left:22px;top:192px;border-radius:40% 40% 20% 20%;background:linear-gradient(#e2767a,#f0d0d0)" role="img" aria-label="Brain with gears"></div>
  <p class="skill" style="left:89px;top:203px">Quantitative<br>Reasoning</p>
  <div class="skill-art" style="left:183px;top:192px;border-radius:50%;background:linear-gradient(135deg,#233a4a,#26a9e0)" role="img" aria-label="Head profile with gears"></div>
  <p class="skill" style="left:244px;top:203px">Concept<br>Integration</p>
</section>

<section class="band relationships">
  <h2 class="heading center row-heading" style="top:31px">Relationships and<br>Communication</h2>
  <div class="row-art" style="left:67px;top:120px;border-radius:12px;background:linear-gradient(#e84a5f 30%,#f7c9a0 31%)" role="img" aria-label="Hand holding a heart"></div>
  <p class="row-item" style="left:22px;top:204px">Cultural<br>Competence</p>
  <div class="row-art" style="left:232px;top:120px;width:42px;border-radius:3px;background:#1e2a3e" role="img" aria-label="Passport with globe"></div>
  <p class="row-item" style="left:177px;top:204px">Service Orientation<br>or Citizenship</p>
  <div class="row-art art" style="left:390px;top:120px;background:#5b8fd1" role="img" aria-label="Group of three colleagues"></div>
  <p class="row-item" style="left:343px;top:204px">Leadership and<br>Teamwork</p>
  <div class="row-art art" style="left:548px;top:120px;width:44px;background:#2f4f6a" role="img" aria-label="Clinician with stethoscope"></div>
  <p class="row-item" style="left:497px;top:204px">Professionalism</p>
</section>

<section class="band growth">
  <h2 class="heading center row-heading" style="top:31px">Intrapersonal<br>Growth</h2>
  <div class="row-art" style="left:77px;top:111px;background:linear-gradient(90deg,#f26b21 20%,#f7c928 20%,#f7c928 45%,#8dd39b 45%,#8dd39b 65%,#0bb04b 65%)" role="img" aria-label="Rising bars with an upward arrow"></div>
  <p class="row-item" style="left:35px;top:196px">Cultural Humility<br>or Sensitivity</p>
  <div class="row-art" style="left:195px;top:111px;border-radius:8px;background:linear-gradient(#f0b323 30%,#6b3a2a 31%)" role="img" aria-label="Balance scales"></div>
  <p class="row-item" style="left:150px;top:196px">Integrity</p>
  <div class="row-art" style="left:318px;top:118px;width:74px;height:45px;border-radius:12px;background:linear-gradient(90deg,#e84a5f 15%,#f5b58a 15%,#f5b58a 85%,#4a86d6 85%)" role="img" aria-label="Handshake"></div>
  <p class="row-item" style="left:279px;top:196px">Self-Directed</p>
  <div class="row-art art" style="left:450px;top:111px;background:conic-gradient(#f04e23,#f7a21b,#ffffff,#1f7ec2,#f04e23)" role="img" aria-label="Circular arrows"></div>
  <p class="row-item" style="left:405px;top:196px">Dependability</p>
  <div class="row-art" style="left:567px;top:111px;background:linear-gradient(transparent 45%,#3b4a66 45%)" role="img" aria-label="Flag on a mountain peak"></div>
  <p class="row-item" style="left:521px;top:196px">Mission<br>Oriented</p>
</section>

</body>
</html>
```